Tree Service Billboard 20x8 ft

We need a billboard design for a tree service company.
The billboard is 20ft x 8 ft so we need a design that is capable to stretching to those dimensions without loosing quality.
I have attached a series of images.
Image 1- Simply a billboard that I think looks good that I would like you to use for inspiration. I am aiming for the same format only no color in the wording, just black white, or gray. I like the the trees in the background, the logo placed to the left, and wording on the right.
Image 2- Current Logo I would like to the left of the billboard
Image 3- Another format of current logo if needed.
Image 4- A drawn out design template
Image 5- Another drawn out design template

Specific things I am looking for
-The contact number to be the largest thing on the design
-The logo on the design
-Key points to the design to say:
Tree Removal
Tree Trimming
Land Development
Stump Grinding
Storm Response
Insured
Free Bids
-The facebook logo
-The Google Logo

```html
<!DOCTYPE html>
<html lang="en">
<head>
<meta charset="utf-8">
<title>Hartwell Tree Service Billboard</title>
<link rel="stylesheet" href="https://fonts.googleapis.com/css2?family=Oswald:wght@400;500&family=Open+Sans:wght@400;600&display=swap">
<style>
  :root {
    --page: #ffffff;
    --ink: #ffffff;
    --ink-soft: rgba(255, 255, 255, 0.85);
    --mist-top: #a7a9a8;
    --mist-mid: #6c7670;
    --forest: #22392c;
    --forest-deep: #172a20;
    --pill: #ffffff;
    --pill-ink: #333333;
    --ghost: rgba(255, 255, 255, 0.22);
  }
  * { margin: 0; padding: 0; box-sizing: border-box; }
  html, body {
    width: 1050px;
    height: 1200px;
    overflow: hidden;
    background: var(--page);
  }
  .billboard {
    position: absolute;
    left: 35px;
    top: 472px;
    width: 980px;
    height: 255px;
    overflow: hidden;
    color: var(--ink);
    font-family: "Oswald", sans-serif;
    box-shadow: 0 6px 14px rgba(0, 0, 0, 0.35);
  }
  .forest-backdrop {
    position: absolute;
    inset: 0;
    background:
      linear-gradient(180deg, var(--mist-top) 0%, var(--mist-mid) 38%, var(--forest) 70%, var(--forest-deep) 100%);
  }
  .logo-mark {
    position: absolute;
    left: 121px;
    top: 14px;
    width: 116px;
    height: 116px;
    border-radius: 50%;
    border: 5px solid var(--ink);
  }
  .ghost-mark {
    position: absolute;
    left: 422px;
    top: 8px;
    width: 168px;
    height: 168px;
    border-radius: 50%;
    border: 6px solid var(--ghost);
  }
  .brand-name {
    position: absolute;
    left: 14px;
    width: 330px;
    top: 138px;
    text-align: center;
    white-space: nowrap;
    font-weight: 500;
    font-size: 30px;
    line-height: 1.1;
    letter-spacing: 0.3px;
  }
  .phone {
    position: absolute;
    left: 30px;
    top: 184px;
    display: flex;
    align-items: center;
    gap: 12px;
    white-space: nowrap;
    font-weight: 400;
    font-size: 48px;
    line-height: 1;
  }
  .phone svg { width: 38px; height: 38px; fill: var(--ink); }
  .social {
    position: absolute;
    left: 377px;
    top: 134px;
    font-family: "Open Sans", sans-serif;
  }
  .social-title {
    font-size: 19px;
    font-weight: 600;
    padding-bottom: 4px;
    border-bottom: 2px solid var(--ink);
    width: 121px;
    margin-bottom: 10px;
  }
  .social-handle {
    display: flex;
    align-items: center;
    width: 121px;
    height: 22px;
    margin-bottom: 7px;
    border-radius: 11px;
    background: var(--pill);
    color: var(--pill-ink);
    font-size: 12px;
  }
  .social-handle .dot {
    width: 22px;
    height: 22px;
    border-radius: 50%;
    background: #555555;
    margin-right: 12px;
    flex: none;
  }
  .visit {
    position: absolute;
    left: 530px;
    top: 176px;
    white-space: nowrap;
  }
  .visit-line {
    font-family: "Open Sans", sans-serif;
    font-size: 16px;
    color: var(--ink-soft);
    line-height: 1.1;
  }
  .visit-name {
    font-weight: 500;
    font-size: 25px;
    line-height: 1.2;
  }
  .services {
    position: absolute;
    right: 26px;
    top: 10px;
    list-style: none;
    text-align: right;
    white-space: nowrap;
  }
  .services li {
    font-weight: 400;
    font-size: 22px;
    line-height: 32.3px;
    letter-spacing: 0.4px;
  }
  .services li::after {
    content: "";
    display: inline-block;
    width: 5px;
    height: 5px;
    background: var(--ink);
    margin-left: 14px;
    vertical-align: middle;
  }
</style>
</head>
<body>
  <section class="billboard">
    <div class="forest-backdrop" role="img" aria-label="Misty evergreen forest on a foggy hillside"></div>

    <div class="ghost-mark" aria-hidden="true"></div>

    <div class="logo-mark" aria-hidden="true"></div>
    <h1 class="brand-name">HARTWELL TREE SERVICE</h1>
    <div class="phone">
      <svg viewBox="0 0 24 24" aria-hidden="true"><path d="M6.6 10.8a15.1 15.1 0 0 0 6.6 6.6l2.2-2.2a1 1 0 0 1 1-.25 11.4 11.4 0 0 0 3.6.57 1 1 0 0 1 1 1V20a1 1 0 0 1-1 1A17 17 0 0 1 3 4a1 1 0 0 1 1-1h3.5a1 1 0 0 1 1 1c0 1.25.2 2.45.57 3.57a1 1 0 0 1-.25 1z"/></svg>
      <span>417-555-0148</span>
    </div>

    <div class="social">
      <p class="social-title">Find us on</p>
      <p class="social-handle"><span class="dot"></span>@acount</p>
      <p class="social-handle"><span class="dot"></span>@acount</p>
    </div>

    <div class="visit">
      <p class="visit-line">Thank for visiting</p>
      <p class="visit-name">HARTWELL TREE SERVICE</p>
    </div>

    <ul class="services">
      <li>TREE REMOVAL</li>
      <li>TREE TRIMMING</li>
      <li>LAND DEVELOPMENT</li>
      <li>STUMP GRINDING</li>
      <li>STORM RESPONSE</li>
      <li>INSURED</li>
      <li>FREE BIDS</li>
    </ul>
  </section>
</body>
</html>
```